electrical automation company needs a letterhead design

we need a letter head designed for our new electrical automation company. Our company color are orange and blue as you'll see from our logo attached

Target Market(s)

Domestic, commercial and industrial electrical clients

Industry/Entity Type

Electrical

Contact Information for Business Card

I need to update my business card to make it more eye catching I have attached my old business card designs, logo and new trifold brochure to give you an idea

Font styles to use
Sans Serif

Colors
f37122
0393ce

Requirements
Must have
• larkfield electrical logo
my name
phone number
email
website
Nice to have
• QR code linked to my website
list of some services
- domestic
- commercial
- industrial

```html
<!DOCTYPE html>
<html lang="en">
<head>
<meta charset="utf-8">
<title>Larkfield Electrical Letterhead</title>
<link href="https://fonts.googleapis.com/css2?family=Open+Sans:wght@400;600;700&display=swap" rel="stylesheet">
<style>
  :root {
    --orange: #f37122;
    --blue: #0393ce;
    --ink: #3a3a3a;
    --paper: #f5f5f5;
    --backdrop: #e2e2e2;
    --rule: #9a9a9a;
  }
  * { box-sizing: border-box; margin: 0; padding: 0; }
  html, body { width: 1200px; height: 945px; overflow: hidden; }
  body {
    background: var(--backdrop);
    font-family: "Open Sans", Arial, sans-serif;
    color: var(--ink);
    position: relative;
  }
  .letterhead {
    position: absolute;
    left: 282px; top: 22px;
    width: 636px; height: 900px;
    background: var(--paper);
    box-shadow: 0 4px 18px rgba(0,0,0,0.12);
  }
  .brand {
    position: absolute; left: 56px; top: 52px;
    display: flex; align-items: center; gap: 10px;
  }
  .brand-mark { width: 22px; height: 22px; background: var(--blue); border-radius: 50%; }
  .brand-name {
    font-size: 19px; font-weight: 700; color: var(--blue);
    text-transform: uppercase; letter-spacing: 0.5px;
  }
  .contact {
    position: absolute; right: 56px; top: 48px;
    font-size: 9.5px; line-height: 1.5;
  }
  .contact-name { color: var(--blue); font-weight: 700; text-transform: uppercase; font-size: 10px; }
  .contact-line { display: flex; align-items: center; gap: 6px; }
  .contact-line svg { width: 9px; height: 9px; fill: var(--blue); }
  .letter-body {
    position: absolute; left: 72px; right: 72px; top: 170px;
    font-size: 12.5px; line-height: 1.32;
  }
  .salutation { font-weight: 700; font-size: 14px; margin-bottom: 14px; }
  .letter-body p { margin-bottom: 16px; }
  .letter-body p.justified { text-align: justify; }
  .signature {
    position: absolute; left: 88px; top: 668px;
    width: 160px; height: 54px;
    background: linear-gradient(90deg, rgba(30,30,30,0.18), rgba(30,30,30,0.06));
    border-radius: 30px;
  }
  .footer { position: absolute; left: 0; right: 0; bottom: 0; height: 90px; }
  .footer-bar { position: absolute; left: 56px; bottom: 24px; width: 10px; height: 40px; background: var(--blue); }
  .services {
    position: absolute; left: 76px; bottom: 46px;
    font-size: 11px; font-weight: 700; color: var(--orange);
    display: flex; gap: 8px;
  }
  .services span::before { content: "• "; color: var(--blue); }
  .footer-rule { position: absolute; left: 76px; right: 210px; bottom: 42px; height: 1px; background: var(--rule); }
  .web-tag {
    position: absolute; right: 40px; bottom: 33px;
    background: var(--blue); color: #fff;
    font-size: 10px; padding: 3px 16px;
    clip-path: polygon(8px 0, 100% 0, calc(100% - 8px) 100%, 0 100%);
  }
</style>
</head>
<body>
  <main class="letterhead">
    <header>
      <div class="brand">
        <span class="brand-mark"></span>
        <span class="brand-name">Larkfield Electrical</span>
      </div>
      <div class="contact">
        <div class="contact-name">Dana Pierce</div>
        <div class="contact-line">
          <svg viewBox="0 0 10 10"><rect x="2.5" y="0.5" width="5" height="9" rx="1"/></svg>
          0400 318 752
        </div>
        <div class="contact-line">
          <svg viewBox="0 0 10 10"><path d="M0 2h10v6H0z M0 2l5 3.5L10 2" stroke="#fff" stroke-width="0.6"/></svg>
          dana@larkfieldelectrical.com.au
        </div>
      </div>
    </header>

    <section class="letter-body">
      <div class="salutation">Dear Mr. Harris,</div>
      <p>Lorem Ipsum is simply dummy text of the printing and typesetting industry. Lorem Ipsum has been the industry's standard dummy text ever since the 1500s, when an unknown printer took a galley of type and scrambled it to make a type specimen book. It has survived not only five centuries, but also the leap into electronic typesetting, remaining essentially unchanged.</p>
      <p class="justified">The standard chunk of Lorem Ipsum used since the 1500s is reproduced below for those interested. Sections 1.10.32 and 1.10.33 from "de Rebus Minimis et Maximis" by Aurelio are also reproduced in their exact original form, accompanied by English versions from the 1914 translation by J. Wendell</p>
      <p>Lorem Ipsum is simply dummy text of the printing and typesetting industry. Lorem Ipsum has been the industry's standard dummy text ever since the 1500s, when an unknown printer took a galley of type and scrambled it to make a type specimen book. It has survived not only five centuries, but also the leap into electronic typesetting, remaining essentially unchanged. It was popularised in the</p>
      <p>Lorem Ipsum is simply dummy text of the printing and typesetting industry. Lorem Ipsum has been the industry's standard dummy text ever since the 1500s, when an unknown printer took a galley of type and scrambled it to make a type specimen book. It has survived not only five centuries, but also the leap into electronic typesetting, remaining essentially unchanged. It was popularised in the</p>
      <p>Lorem Ipsum is simply dummy text of the printing and typesetting industry. Lorem Ipsum has been the industry's standard dummy text ever since the 1500s, when an unknown printer took a galley of type and scrambled it to make a type specimen book.</p>
    </section>

    <div class="signature" role="img" aria-label="Handwritten signature of the sender"></div>

    <footer class="footer">
      <div class="footer-bar"></div>
      <div class="services"><span>Domestic</span><span>Commercial</span><span>Industrial</span></div>
      <div class="footer-rule"></div>
      <div class="web-tag">www.larkfieldelectrical.com.au</div>
    </footer>
  </main>
</body>
</html>
```